Dynamic Lead Design (Partial WebPage)

To encourage visitors to our website to donate to our organization, we would like to replace the Dynamic Lead on our website with one that will evoke emotion from the viewer and motivate them to donate generously.

The deliverable should be a mockup of the design in context of the current website. See attached file for editable area. Fonts used in the mockup should be code-able in HTML/CSS.

The website
http://www.tumorhope.org

Please use this wireframe for reference:
http://app.wiredraftly.com/8b1c47d2e09f3a5561c7d4e0a2b9f8c3d7e61a04/7718264

Content:
[Image should evoke emotion from the viewer and motivate them to donate generously.]
Headline - “Give to HAVEN.”
Sub Headline - “Cancer patients find answers here. Your donation makes that possible.”
Call to action label - “Donate”

We love these examples:

Mt. Orwell Hearts and Sharing (http://www.hs.mtorwell.org/mtorwell/v/index.jsp?vgnextoid=7a5d21f0c3b9e4d8VgnVCM100000481726bdRCRD)
Kindly Wells (http://www.kindlywells.org/)

Design Size:
width: 971px
height: 300px

***see attached document for design area***

- Organization Background -

Our website receives over 40,000 unique visitors each month - mostly cancer patients and their family members seeking information about their disease. We would like to drive our visitors to donate to our nonprofit throughout late November and December (the majority of our donations from individuals come in during that time period).

We will be mailing an appeal letter to our database in mid-November. With this banner ad, we seek to complement that appeal. Some key messages from our appeal are:

- We focus on getting patients and their loved ones the best, most up-to-date information from trusted doctors who are leaders in cancer research – for free. We don’t sell a particular product or procedure. We simply arm them with the most current information so they can make the best decision for their own (or their loved one’s) care.

- What is the value of the support they or someone they know has received from our organization? Twenty-five dollars? One hundred dollars? One thousand? Can you even put an amount to it? Whatever it is, please consider making an end of year donation to this organization that has helped so many, comforted hundreds of thousands of patients and caretakers, and been there when needed.

- 2014 will be a year of growth. We just hired our first executive director. She is experienced in helping small nonprofits grow in size, revenue, and scope, and will undoubtedly bring a new level of energy to our work.

- In just a few months, we will hold two patient forums – first-of-its-kind programs for the organization. As we continue to grow, we will be able to offer more of these types of programs to more patients throughout the US.

Industry/Entity Type

Charity

Requirements
Must have
• - Must Adhere to existing website branding

```html
<!DOCTYPE html>
<html lang="en">
<head>
<meta charset="utf-8">
<title>HAVEN – Give to HAVEN</title>
<link rel="stylesheet" href="https://fonts.googleapis.com/css2?family=Source+Sans+3:wght@400;600;700&family=Varela+Round&display=swap">
<style>
:root{
  --green:#8fcfa7;
  --green-dark:#4a8a3e;
  --salmon:#e39a83;
  --salmon-dark:#d9826a;
  --slate:#77787b;
  --band-dark:#8d8d8d;
  --band-mid:#d3d3d3;
  --band-light:#e7e7e7;
  --text:#2b2b2b;
  --heading:#6d6e70;
  --taupe:#9b8f86;
  --rule:#dcdcdc;
  --white:#ffffff;
}
*{box-sizing:border-box;margin:0;padding:0}
html,body{width:1047px;height:1200px;overflow:hidden;background:var(--white)}
body{position:relative;font-family:Arial,Helvetica,sans-serif;color:var(--text)}
a{text-decoration:none;color:inherit}
.abs{position:absolute}

/* header */
.brand{left:44px;top:44px;display:flex;align-items:center;gap:14px}
.brand-dot{width:64px;height:64px;border-radius:50%;background:var(--salmon)}
.brand-name{font-family:"Source Sans 3",sans-serif;font-weight:700;font-size:40px;color:var(--salmon);letter-spacing:1px}
.search{left:470px;top:44px;width:399px;height:60px;border:5px solid #cfe9d8;border-radius:30px;background:#f4faf6;display:flex;align-items:center;padding:0 14px;gap:6px}
.search-field{flex:1;height:26px;border:1px solid #bbb;background:var(--white);font-size:10px;color:#999;padding:6px}
.search-btn{background:var(--green);font-size:11px;font-weight:bold;color:#2f5e3c;padding:6px 8px;border-radius:2px}
.search-x{font-size:12px;color:#777}

/* navigation */
.nav{left:44px;top:150px;width:960px;height:45px;display:flex;gap:3px}
.nav-tab{flex:1;display:flex;align-items:center;justify-content:center;text-align:center;background:var(--green);color:var(--white);font-family:"Source Sans 3",sans-serif;font-weight:600;font-size:16px;letter-spacing:1px;line-height:15px;text-transform:uppercase}
.nav-tab.small{font-size:14px}
.nav-tab.profile{background:var(--slate)}
.nav-tab.donate{background:var(--salmon)}
.donate-tab-cap{left:940px;top:114px;width:64px;height:40px;background:var(--salmon);border-radius:22px 22px 0 0}
.donate-tab-cap svg{position:absolute;left:18px;top:6px}

/* hero lead */
.hero{left:44px;top:206px;width:960px;height:287px;background:var(--band-light)}
.hero-photo{left:60px;top:208px;width:411px;height:274px;background:linear-gradient(110deg,#3a3a3a,#9a9a9a 45%,#d8d8d8 70%,#7a7a7a);border:2px solid #444}
.hero-headline{left:472px;top:208px;width:532px;height:97px;background:var(--band-dark);color:var(--white);font-family:"Source Sans 3",sans-serif;font-weight:600;font-size:66px;line-height:97px;padding-left:32px;letter-spacing:-0.5px}
.hero-sub{left:472px;top:305px;width:532px;height:84px;background:var(--band-mid);color:#1f1f1f;font-family:"Source Sans 3",sans-serif;font-weight:600;font-size:29px;line-height:36px;padding:6px 0 0 35px}
.hero-cta{left:608px;top:412px;width:258px;height:59px;border-radius:30px;background:linear-gradient(#6a6a6a,#262626);border:2px solid #9a9a9a;color:var(--white);font-family:"Source Sans 3",sans-serif;font-weight:700;font-size:26px;display:flex;align-items:center;justify-content:center;letter-spacing:.5px}

/* main column */
.edit-link{left:56px;top:509px;font-size:14px;font-weight:bold}
.section-title{left:44px;top:569px;font-size:18px;font-weight:bold;color:var(--heading)}
.share-bar{left:515px;top:558px;width:193px;height:17px;border:1px solid #c66;display:flex;align-items:center;gap:2px;padding:0 3px;font-size:12px;color:#222}
.share-bar i{display:inline-block;width:11px;height:11px;background:#999}
.share-bar span{margin-left:3px}
.post{left:44px;width:681px}
.post-title{font-size:17px;font-weight:bold;color:var(--green-dark);line-height:21px}
.post-meta{font-size:13px;margin-top:4px}
.post-meta a{color:var(--green-dark);font-weight:bold}
.post-meta b{font-weight:bold}
.post-excerpt{font-size:14.5px;line-height:21px;margin-top:14px}
.post-excerpt em{color:var(--green-dark);font-size:13px}
.rule{left:44px;width:681px;height:1px;background:var(--rule)}

/* sidebar */
.social{left:776px;top:514px;display:flex;gap:30px}
.social i{display:block;width:30px;height:30px;border-radius:3px;background:#b9c3cc}
.ask-box{left:750px;top:566px;width:240px;height:44px;background:var(--salmon);border-radius:4px;display:flex;align-items:center;padding-left:10px;gap:6px;color:var(--white);font-family:"Varela Round",sans-serif;font-size:20px}
.ask-box .bubble{width:28px;height:28px;border-radius:50%;background:#c8806b;font-size:13px;display:flex;align-items:center;justify-content:center}
.ask-box .label{margin-left:22px;letter-spacing:1px}
.side-heading{left:750px;top:636px;font-size:17px;font-weight:bold;color:var(--heading)}
.side-link{left:750px;font-size:12.5px;font-weight:bold;color:var(--green-dark)}
.forum-box{left:750px;top:748px;width:240px;height:44px;background:var(--salmon);border-radius:4px;color:var(--white);font-family:"Varela Round",sans-serif;font-size:17px;line-height:19px;text-align:center;padding-top:3px;letter-spacing:1px}
.faculty{left:750px;top:898px;width:240px;height:138px;background:linear-gradient(135deg,#8a7a6c,#c9b8a4 50%,#6f6258)}
.faculty-note{left:786px;top:935px;width:170px;height:58px;background:#f7e9dc;color:var(--salmon-dark);font-family:"Varela Round",sans-serif;font-size:12.5px;line-height:14px;text-align:center;padding-top:2px}
.faculty-note b{color:var(--green-dark)}
.cancer-list{left:750px;top:1062px;width:240px;display:flex;flex-direction:column;gap:2px}
.cancer-list a{display:block;height:22px;background:var(--taupe);color:var(--white);text-align:center;font-family:"Varela Round",sans-serif;font-size:15px;line-height:22px;border-radius:2px}
</style>
</head>
<body>

<header>
  <a class="abs brand" href="http://www.tumorhope.org"><span class="brand-dot"></span><span class="brand-name">HAVEN</span></a>
  <form class="abs search"><div class="search-field">Site Search</div><span class="search-btn">Search</span><span class="search-x">✕</span></form>
  <div class="abs donate-tab-cap"><svg width="28" height="28" viewBox="0 0 28 28"><circle cx="14" cy="14" r="12" fill="#fff"/><path d="M14 8v12M8 14h12" stroke="#6cbf84" stroke-width="3"/></svg></div>
  <nav class="abs nav">
    <a class="nav-tab">About HAVEN</a>
    <a class="nav-tab small">Ask Us<br>Discussion Forums</a>
    <a class="nav-tab small">General<br>Cancer Info</a>
    <a class="nav-tab small">Focused<br>Cancer Info</a>
    <a class="nav-tab profile">Profile</a>
    <a class="nav-tab donate">Donate</a>
  </nav>
</header>

<section>
  <div class="abs hero"></div>
  <div class="abs hero-photo" role="img" aria-label="Black and white photo of a smiling young cancer patient touching their head"></div>
  <h1 class="abs hero-headline">Give to HAVEN.</h1>
  <p class="abs hero-sub">Cancer patients find answers here.<br>Your donation makes that possible.</p>
  <a class="abs hero-cta">DONATE NOW</a>
</section>

<main>
  <a class="abs edit-link">Edit</a>
  <h2 class="abs section-title">Recent HAVEN News &amp; Posts</h2>
  <div class="abs share-bar"><i></i><i></i><i></i><i></i><span>Share/Email/More</span></div>

  <article class="abs post" style="top:636px">
    <h3 class="post-title">Cancer Care In Crisis? The Council on Health Standards' Report: Delivering High-Quality Cancer Care: Charting a New Course For a System in Crisis; Part I: The Current Landscape</h3>
    <p class="post-meta"><b>by</b> <b>Dr. Kessler</b> <b>on</b> Nov 10, 2013 <b>in</b> <a>HAVEN :: Cancer Basics</a></p>
    <p class="post-excerpt">&nbsp;A few months ago, the Council on Health Standards released the prepublication proofs of a massive report on the state of oncology care, saying that it was in crisis in the United States. I learned about it from an email that focused on the crisis part of the title. I was bo... <em>(Read More)</em></p>
  </article>
  <div class="abs rule" style="top:824px"></div>

  <article class="abs post" style="top:853px">
    <h3 class="post-title">Is there a place for live educational meetings in our new online world? Would you want to come?</h3>
    <p class="post-meta"><b>by</b> <b>Dr Lane</b> <b>on</b> Nov 8, 2013 <b>in</b> <a>HAVEN :: Lung Cancer</a></p>
    <p class="post-excerpt">Back in 2009, HAVEN did a live educational meeting in Seattle, geared toward patients and caregivers, that coincided with a lung cancer conference offered to physicians. It included brief (~15 minute) talks by about 10 different specialists, ranging in topics from initi... <em>(Read More)</em></p>
  </article>
  <div class="abs rule" style="top:1020px"></div>

  <article class="abs post" style="top:1048px">
    <h3 class="post-title">Tweet Chat Thursday: The Tissue is the Issue, Key Challenges in Biopsies and Tissue Collection</h3>
    <p class="post-meta"><b>by</b> <b>Dr Lane</b> <b>on</b> Nov 5, 2013 <b>in</b> <a>HAVEN :: Lung Cancer</a></p>
    <p class="post-excerpt">This Thursday, November 7th at 8 PM Eastern, 5 PM Pacific, we'll gather in the Chatverse for another one hour #LCHV (lung cancer haven voices) tweet chat. This time, the topic will be on biopsies and tissue collection.&nbsp; Now that we've entered a new era where more an... <em>(Read More)</em></p>
  </article>
</main>

<aside>
  <div class="abs social"><i></i><i></i><i></i><i></i></div>
  <div class="abs ask-box"><span class="bubble">Q:</span><span class="bubble">A:</span><span class="label">Ask Us</span></div>
  <h3 class="abs side-heading">Welcome To HAVEN!</h3>
  <a class="abs side-link" style="top:666px">How To Use HAVEN</a>
  <a class="abs side-link" style="top:687px">General Cancer FAQs</a>
  <a class="abs side-link" style="top:714px">Recent HAVEN Site Post Comments</a>
  <div class="abs forum-box">HAVEN<br>Discussion Forums</div>
  <a class="abs side-link" style="top:805px">HAVEN Discussion Forum Guidelines</a>
  <a class="abs side-link" style="top:831px">Recent HAVEN Forum Activity</a>
  <a class="abs side-link" style="top:858px">Original HAVEN Archived Forums</a>
  <div class="abs faculty" role="img" aria-label="Grid of faculty member portrait photos"></div>
  <div class="abs faculty-note">HAVEN is eager to bring in more great faculty members...<br><b>Interested? Click Here!</b></div>
  <nav class="abs cancer-list">
    <a>Lung/Thoracic Cancer Info</a>
    <a>Breast Cancer Info</a>
    <a>Pancreatic Cancer Info</a>
    <a>Kidney Cancer Info</a>
    <a>Bladder Cancer Info</a>
    <a>Head/Neck Cancer Info</a>
  </nav>
</aside>

</body>
</html>
```